We have a parent company, Summit Harbor Group (SHG), that has other company partners. We are looking for ways to incorporate our SHG logo with our network partners, Beacon Ledger and The Blue Gate. My initial thought is to have SHG as front of card logo, and include The Blue Gate and Beacon Ledger logos on back but I'm open to ideas. Card should include website www.summitharborgrp.example (use for reference). Keywords "Tax Services" "Real Estate" "Insurance" "Investments" "Chief Financial Officer"

Industry/Entity Type

Financial

```html
<!DOCTYPE html>
<html lang="en">
<head>
<meta charset="utf-8">
<title>Summit Harbor Group – Business Card</title>
<link href="https://fonts.googleapis.com/css2?family=Source+Sans+3:wght@400;600;700&display=swap" rel="stylesheet">
<style>
  :root {
    --backdrop: #d1d2d4;
    --card: #ffffff;
    --ink: #231f20;
    --brand-blue: #0b56a4;
    --brand-red: #e8202a;
  }
  * { margin: 0; padding: 0; box-sizing: border-box; }
  html, body { width: 1200px; height: 1200px; overflow: hidden; }
  body {
    background: var(--backdrop);
    font-family: "Source Sans 3", "Myriad Pro", sans-serif;
    color: var(--ink);
    position: relative;
  }
  .card {
    position: absolute;
    left: 290px;
    width: 625px;
    height: 356px;
    background: var(--card);
  }
  .card--front { top: 220px; }
  .card--back { top: 688px; }

  .holder {
    position: absolute;
    top: 64px;
    left: 0;
    width: 100%;
    text-align: center;
  }
  .holder__name {
    font-size: 34px;
    line-height: 1;
    letter-spacing: -0.5px;
    font-weight: 400;
  }
  .holder__name strong { font-weight: 700; }
  .holder__title {
    margin-top: 6px;
    font-size: 19px;
    letter-spacing: 0.2px;
  }

  .contact {
    position: absolute;
    top: 192px;
    width: 180px;
    margin-left: -90px;
    text-align: center;
    font-size: 16px;
    line-height: 21px;
    white-space: nowrap;
  }
  .contact__icon {
    display: block;
    margin: 0 auto 20px;
    height: 48px;
  }
  .contact--phone { left: 124px; }
  .contact--email { left: 309px; }
  .contact--address { left: 496px; }

  .front-rule {
    position: absolute;
    left: 20px;
    right: 20px;
    top: 326px;
    height: 10px;
    background: var(--brand-blue);
  }

  .brand {
    position: absolute;
    top: 140px;
    left: 0;
    width: 100%;
    display: flex;
    justify-content: center;
    align-items: center;
    gap: 14px;
  }
  .brand__dot {
    width: 30px;
    height: 30px;
    border-radius: 50%;
    background: var(--brand-red);
  }
  .brand__name {
    font-size: 34px;
    font-weight: 600;
    color: var(--brand-blue);
    letter-spacing: 0.5px;
  }

  .web-band {
    position: absolute;
    left: 20px;
    right: 20px;
    top: 282px;
    height: 54px;
    background: var(--brand-blue);
    color: #ffffff;
    display: flex;
    align-items: center;
    justify-content: center;
    font-size: 17px;
    letter-spacing: 3px;
    text-transform: uppercase;
  }
</style>
</head>
<body>
  <section class="card card--front">
    <div class="holder">
      <h1 class="holder__name"><strong>JOHN</strong> DOE</h1>
      <p class="holder__title">DESIGNATION</p>
    </div>

    <div class="contact contact--phone">
      <svg class="contact__icon" viewBox="0 0 48 48" width="48" height="48" aria-hidden="true">
        <path d="M9 6c2-1 4-1 5 1l4 7c1 2 0 3-1 4l-2 2c2 5 6 9 11 11l2-2c1-1 3-2 4-1l7 4c2 1 2 3 1 5l-2 3c-2 2-5 3-8 2C18 38 10 30 6 18c-1-3 0-6 2-8z" fill="var(--ink)"/>
      </svg>
      <p>555.010.0142<br>555.010.0142</p>
    </div>

    <div class="contact contact--email">
      <svg class="contact__icon" viewBox="0 0 48 48" width="48" height="48" aria-hidden="true">
        <rect x="2" y="9" width="44" height="30" fill="var(--ink)"/>
        <path d="M4 11l20 16 20-16M4 37l15-13M44 37L29 24" stroke="#fff" stroke-width="2" fill="none"/>
      </svg>
      <p>info@shg.example<br>name@shg.example</p>
    </div>

    <div class="contact contact--address">
      <svg class="contact__icon" viewBox="0 0 48 48" width="48" height="48" aria-hidden="true">
        <path d="M24 3L3 20h42z" fill="var(--ink)"/>
        <rect x="8" y="5" width="4" height="8" fill="var(--ink)"/>
        <path d="M7 22h34v20H7z M16 28v14h16V28z" fill="var(--ink)" fill-rule="evenodd"/>
        <rect x="20" y="30" width="8" height="12" fill="var(--ink)"/>
        <rect x="3" y="44" width="42" height="3" fill="var(--ink)"/>
      </svg>
      <p>1200 Harbor Way<br>Lakeside, CO 80000</p>
    </div>

    <div class="front-rule"></div>
  </section>

  <section class="card card--back">
    <div class="brand">
      <span class="brand__dot" aria-hidden="true"></span>
      <span class="brand__name">Summit Harbor Group</span>
    </div>
    <div class="web-band">www.summitharborgrp.example</div>
  </section>
</body>
</html>
```